ROV Medisource Website design
Website design
ROV Medisource Website design -
Creative Brief
www.rovmedisource.example
Leading exporter for used medical equipments world wide
Like it to me clean and simple
left side
http://www.bluvantor.example/ http://www.torrelinkmd.example/index.html http://www.quovarent.example/en.html http://www.halbrit.example/ http://www.wellgatehub.example/ http://www.vintrosa.example/home http://www.carelodgex.example/ http://www.dorum.example/ http://www.ferntonmed.example/ http://www.zavrimedix.example/ http://www.pinehursthomes.example/ http://www.gluvatrade.example/component/page,shop.browse/category_id,8/option,com_virtuemart/Itemid,64/ (Left hand Navigation for Equipment page)

```html
<!DOCTYPE html>
<html lang="en">
<head>
<meta charset="utf-8">
<title>ROV Medisource</title>
<link href="https://fonts.googleapis.com/css2?family=Arimo:wght@400;700&display=swap" rel="stylesheet">
<style>
:root{
  --page-bg:#eeeeee;
  --card:#ffffff;
  --border:#d6d6d6;
  --ink:#333333;
  --muted:#666666;
  --blue:#1a75b8;
  --blue-dark:#0d4f86;
  --green:#5c9b1e;
  --green-light:#8cc63f;
  --hero-a:#dfe7ec;
  --hero-b:#a9bccb;
}
*{box-sizing:border-box;margin:0;padding:0}
html,body{width:1200px;height:921px;overflow:hidden}
body{background:var(--page-bg);font-family:"Arimo",Arial,sans-serif;color:var(--ink);position:relative}
.site{position:absolute;left:137px;top:37px;width:946px;height:809px;background:var(--card);border:1px solid var(--border);box-shadow:0 0 6px rgba(0,0,0,.08)}
.brand{position:absolute;left:20px;top:22px;display:flex;align-items:center;gap:10px}
.brand-dot{width:46px;height:46px;border-radius:50%;background:var(--blue)}
.brand-name{font-size:26px;font-weight:700;color:var(--blue-dark)}
.main-nav{position:absolute;left:290px;top:33px;width:639px;height:42px;border:1px solid var(--border);border-radius:3px;display:flex;align-items:center;justify-content:center;font-size:13.5px;font-weight:700;color:var(--blue-dark)}
.main-nav span{padding:0 11px}
.main-nav .sep{padding:0;color:#999;font-weight:400}
.hero{position:absolute;left:5px;top:100px;width:934px;height:319px;overflow:hidden}
.hero-photo{position:absolute;inset:0;background:linear-gradient(100deg,#f4f7f9 0%,var(--hero-a) 40%,var(--hero-b) 100%)}
.hero-swoosh{position:absolute;left:0;top:0}
.hero-title{position:absolute;left:42px;top:155px;font-size:34px;line-height:40px;color:var(--blue)}
.pager{position:absolute;right:14px;bottom:16px;display:flex;gap:5px}
.pager span{width:24px;height:24px;border-radius:50%;background:var(--blue);color:#fff;font-size:13px;font-weight:700;display:flex;align-items:center;justify-content:center}
.pager .active{background:var(--green)}
.features{position:absolute;left:12px;top:440px;width:920px;height:250px;display:flex}
.feature{position:relative;width:240px;padding:10px 14px 0 10px;border-left:1px solid #ececec}
.feature:first-child{border-left:none;width:205px}
.feature h2{font-size:17px;color:var(--green);margin-bottom:10px}
.feature p{font-size:11.5px;line-height:14.6px;text-align:justify;color:var(--muted)}
.feature ul{list-style:none;font-size:12px;color:var(--muted)}
.feature li{line-height:27px;padding-left:12px;position:relative}
.feature li::before{content:"";position:absolute;left:0;top:11px;width:5px;height:5px;background:var(--green-light)}
.learn-more{position:absolute;right:14px;top:228px;width:92px;height:20px;border:1px solid #c8c8c8;border-radius:3px;background:linear-gradient(#fff,#e6e6e6);font-size:9px;font-weight:700;color:var(--blue-dark);display:flex;align-items:center;justify-content:center;gap:4px}
.footer{position:absolute;left:12px;right:12px;top:727px;border-top:1px solid var(--border);padding-top:20px}
.footer-nav{font-size:11.5px;color:var(--muted)}
.footer-nav span{padding:0 4px}
.copyright{font-size:11.5px;color:var(--muted);margin-top:10px;padding-left:4px}
.social{position:absolute;right:4px;top:14px;display:flex;gap:6px}
.social span{width:22px;height:22px;border-radius:3px}
</style>
</head>
<body>
<div class="site">
  <div class="brand"><span class="brand-dot"></span><span class="brand-name">ROV Medisource</span></div>
  <nav class="main-nav">
    <span>Home</span><span class="sep">|</span><span>About Us</span><span class="sep">|</span><span>Our Services</span><span class="sep">|</span><span>Equipment</span><span class="sep">|</span><span>Planning &amp; Consulting</span><span class="sep">|</span><span>Contact Us</span>
  </nav>
  <section class="hero">
    <div class="hero-photo" role="img" aria-label="Clinician operating a CT scanner with a patient on the table"></div>
    <svg class="hero-swoosh" width="934" height="60" viewBox="0 0 934 60"><path d="M0 30 Q300 0 934 12" fill="none" stroke="#8cc63f" stroke-width="3"/><path d="M0 0 H934 V12 Q300 0 0 30 Z" fill="#fff"/></svg>
    <h1 class="hero-title">Comprehensive<br>Services Worldwide...</h1>
    <div class="pager"><span>1</span><span>2</span><span class="active">3</span><span>4</span></div>
  </section>
  <section class="features">
    <div class="feature">
      <h2>Equipment</h2>
      <ul>
        <li>Lorem ipsum dummy</li><li>Dummy text</li><li>Lorem ipsum Lorem</li><li>Ipsum dummy</li><li>This is dummy text</li><li>Lorem ipsum dummy</li><li>Lorem ipsum text</li>
      </ul>
    </div>
    <div class="feature">
      <h2>Accessories &amp; Parts</h2>
      <p>ROV Medisource is the leading multi-manufacturer,multi-modality alternative parts supplier worldwide. We support both Imaging and Biomed parts for over 2000 makes &amp; models. We offer quick turnaround time and a variety of new, refurbished and used parts pricing options saving customers 25-50% off current OEM parts pricing</p>
      <span class="learn-more">LEARN MORE <svg width="8" height="8" viewBox="0 0 8 8"><path d="M2 1 L6 4 L2 7" fill="none" stroke="#0d4f86" stroke-width="1.5"/></svg></span>
    </div>
    <div class="feature">
      <h2>Planning &amp; Consulting</h2>
      <p>ROV Medisource is the leading international provider of Healthcare Equipment Planning and Consulting services worldwide. Backed by a team of seasoned National &amp; International specialists, ROV Medisource develop turnkey project solutions, from the design stage to production based on your needs. Our Solutions Teams</p>
      <span class="learn-more">LEARN MORE <svg width="8" height="8" viewBox="0 0 8 8"><path d="M2 1 L6 4 L2 7" fill="none" stroke="#0d4f86" stroke-width="1.5"/></svg></span>
    </div>
    <div class="feature">
      <h2>About ROV</h2>
      <p>ROV Medisource is the leading full-service provider of Refurbished and Certified pre-owned Medical equipments worldwide. We serve private clinics, imaging centers, hospitals, Biomed shops, ISO's throughout the U.S. and around the world. As an industry leader, we are known for integrity, expertise and cost effective approach in an increasingly complex industry</p>
      <span class="learn-more">LEARN MORE <svg width="8" height="8" viewBox="0 0 8 8"><path d="M2 1 L6 4 L2 7" fill="none" stroke="#0d4f86" stroke-width="1.5"/></svg></span>
    </div>
  </section>
  <footer class="footer">
    <div class="footer-nav"><span>Home</span>|<span>About Us</span>|<span>Our Services</span>|<span>Equipment</span>|<span>Planning &amp; Consulting</span>|<span>Accessories &amp; Parts</span>|<span>Contact Us</span></div>
    <div class="copyright">Copyright © 2003-2011 ROVMedisource.com. All Rights Reserved.</div>
    <div class="social"><span style="background:#3b5a9a"></span><span style="background:#3aa7e0"></span><span style="background:#7aa3c8"></span><span style="background:#c9302c"></span></div>
  </footer>
</div>
</body>
</html>
```